Brochure Design for Finance Company

We are looking for 2 double-sided A4 brochures.
We are a Scandinavian finance company now operating in Australia. The main service we provide, and which the brochures are for, is Invoice Factoring. While invoice factoring isn’t new, the way we let our clients factor their invoices is. We have simply made Invoice Factoring simple, and we need the brochures to reflect that.
Brochure 1: Why Invoice Factoring
This brochure is meant for potential clients who have never heard of Invoice Factoring before. It should communicate business growth and speeding up cash flow.
Brochure 2: Why Us
This brochure explains how our service differs from our competitors. It should communicate how simple and easy it is to use our service.
We aim to be seen as professional but approachable, and our design language is minimalist as per our Scandinavian heritage.
I will attach our logo as well as some of the graphics we use. Feel free to look at www.travicorfinance.com.au for more inspiration.
Industry/Entity Type
Finance
Look and feel

```html
<!DOCTYPE html>
<html lang="en">
<head>
<meta charset="utf-8">
<title>Travicor Finance – Invoice Factoring</title>
<link href="https://fonts.googleapis.com/css2?family=Roboto+Condensed:wght@400;700&family=Open+Sans:wght@400;600;700&display=swap" rel="stylesheet">
<style>
  :root {
    --brand-blue: #1b7fae;
    --brand-blue-dark: #0d5670;
    --accent-orange: #f07a2e;
    --ink: #1a1a1a;
    --body-ink: #2b2b2b;
    --panel-top: #ffffff;
    --panel-bottom: #dcebf3;
    --grid-line: #e3e6ea;
    --paper: #ffffff;
  }
  * { box-sizing: border-box; margin: 0; padding: 0; }
  html, body { width: 849px; height: 1200px; overflow: hidden; background: var(--paper); }
  .brochure { position: relative; width: 849px; height: 1200px; background: var(--paper); font-family: "Open Sans", Arial, sans-serif; color: var(--body-ink); overflow: hidden; }

  .hero-chart { position: absolute; left: 0; top: 0; width: 849px; height: 560px; }
  .hero-person { position: absolute; left: 95px; top: 0; width: 340px; height: 470px;
    background: linear-gradient(160deg, #3a3d44 0%, #25272c 55%, #4a3a30 100%);
    border-radius: 0 0 40px 60px; opacity: .92; }

  .brand { position: absolute; right: 38px; top: 48px; display: flex; align-items: center; gap: 12px; }
  .brand-dot { width: 40px; height: 40px; border-radius: 50%; background: var(--brand-blue); }
  .brand-name { font-family: "Open Sans", Arial, sans-serif; font-weight: 700; font-size: 30px; color: var(--brand-blue); letter-spacing: .5px; }

  .call-box { position: absolute; left: 460px; top: 460px; width: 389px; height: 100px; background: var(--brand-blue);
    color: #fff; font-family: "Roboto Condensed", Arial, sans-serif; font-weight: 700; text-align: center; padding-top: 12px; }
  .call-box .label { font-size: 30px; line-height: 36px; }
  .call-box .phone { font-size: 32px; line-height: 40px; letter-spacing: .5px; }
  .call-fold { position: absolute; left: 460px; top: 560px; }

  .headline { position: absolute; left: 47px; top: 612px; width: 780px; font-family: "Roboto Condensed", Arial, sans-serif;
    font-weight: 700; font-size: 45px; line-height: 54px; color: var(--ink); }

  .intro { position: absolute; left: 47px; top: 746px; width: 318px; font-size: 10.6px; line-height: 15.4px; }
  .intro p + p { margin-top: 15px; }

  .benefits { position: absolute; left: 378px; top: 749px; width: 425px; height: 244px; border-radius: 10px;
    background: linear-gradient(180deg, var(--panel-top) 0%, var(--panel-bottom) 100%); padding: 14px 0 0 20px; list-style: none; }
  .benefits li { display: flex; align-items: center; gap: 10px; height: 28px; font-size: 13.6px; font-weight: 600; color: var(--brand-blue); }
  .benefits svg { flex: none; }

  .stats { position: absolute; left: 47px; top: 1018px; width: 760px; display: flex; }
  .stat { flex: 1; text-align: center; padding: 4px 0; }
  .stat + .stat { border-left: 1px solid var(--grid-line); }
  .stat .figure { font-family: "Roboto Condensed", Arial, sans-serif; font-weight: 700; font-size: 40px; line-height: 44px; color: var(--brand-blue); }
  .stat .caption { font-size: 15px; line-height: 20px; color: var(--accent-orange); font-weight: 600; }

  .payout-note { position: absolute; left: 0; top: 1130px; width: 849px; text-align: center; font-size: 15px; font-weight: 600; color: var(--brand-blue); }

  .footer-bar { position: absolute; left: 0; top: 1159px; width: 849px; height: 41px; background: var(--brand-blue);
    color: #fff; font-weight: 700; font-size: 15px; line-height: 41px; text-align: right; padding-right: 40px; }
</style>
</head>
<body>
<main class="brochure">

  <svg class="hero-chart" viewBox="0 0 849 560" aria-hidden="true">
    <g stroke="var(--grid-line)" stroke-width="1.5" fill="none">
      <path d="M40 480 H720 M40 440 H720 M40 400 H720 M40 360 H720 M40 320 H720 M40 280 H720 M40 240 H720"/>
      <path d="M80 240 V480 M160 240 V480 M240 240 V480 M320 240 V480 M400 240 V480 M480 240 V480 M560 240 V480 M640 240 V480 M720 240 V480"/>
    </g>
    <polyline points="0,520 60,480 200,470 280,405 420,400 520,330 600,300 680,230" fill="none" stroke="var(--accent-orange)" stroke-width="16" stroke-linejoin="round"/>
    <polygon points="650,200 720,180 690,250" fill="var(--accent-orange)"/>
  </svg>
  <div class="hero-person" role="img" aria-label="Photo of a businessman in a suit carrying a laptop, stepping up the rising orange growth arrow"></div>

  <div class="brand">
    <span class="brand-dot"></span>
    <span class="brand-name">Travicor Finance</span>
  </div>

  <div class="call-box">
    <div class="label">CALL NOW</div>
    <div class="phone">+61(0)2 9284 1736</div>
  </div>
  <svg class="call-fold" width="44" height="34" viewBox="0 0 44 34" aria-hidden="true">
    <polygon points="0,0 44,0 44,34" fill="var(--brand-blue-dark)"/>
  </svg>

  <h1 class="headline">The secret to growing your business faster is to get your invoices paid faster.</h1>

  <div class="intro">
    <p>These days, servicing your clients or customers can often be just half the job. Unfortunately, getting paid promptly can be the other half.</p>
    <p>In fact today’s tough economic climate means more and more businesses are deliberately stretching out the time they take to pay their suppliers. Like most small businesses you’re probably far too familiar with how much longer you’re being made to wait for your invoices to be paid.</p>
    <p>And not only can slow payers add to your workload and cause you sleepless nights but they’re also stopping your business from thriving and growing as fast as its real potential should allow.</p>
  </div>

  <ul class="benefits">
    <li><svg width="14" height="12" viewBox="0 0 14 12"><path d="M1 6 L5 10 L13 1" fill="none" stroke="var(--accent-orange)" stroke-width="2.4"/></svg>With Travicor, being new is OK</li>
    <li><svg width="14" height="12" viewBox="0 0 14 12"><path d="M1 6 L5 10 L13 1" fill="none" stroke="var(--accent-orange)" stroke-width="2.4"/></svg>More time to focus on your core business</li>
    <li><svg width="14" height="12" viewBox="0 0 14 12"><path d="M1 6 L5 10 L13 1" fill="none" stroke="var(--accent-orange)" stroke-width="2.4"/></svg>Access the cash you need, when you need it</li>
    <li><svg width="14" height="12" viewBox="0 0 14 12"><path d="M1 6 L5 10 L13 1" fill="none" stroke="var(--accent-orange)" stroke-width="2.4"/></svg>Free up cash to buy more stock</li>
    <li><svg width="14" height="12" viewBox="0 0 14 12"><path d="M1 6 L5 10 L13 1" fill="none" stroke="var(--accent-orange)" stroke-width="2.4"/></svg>Cash in on your healthy assets</li>
    <li><svg width="14" height="12" viewBox="0 0 14 12"><path d="M1 6 L5 10 L13 1" fill="none" stroke="var(--accent-orange)" stroke-width="2.4"/></svg>Get the best possible payout rate</li>
    <li><svg width="14" height="12" viewBox="0 0 14 12"><path d="M1 6 L5 10 L13 1" fill="none" stroke="var(--accent-orange)" stroke-width="2.4"/></svg>You choose when and how many invoices you sell</li>
    <li><svg width="14" height="12" viewBox="0 0 14 12"><path d="M1 6 L5 10 L13 1" fill="none" stroke="var(--accent-orange)" stroke-width="2.4"/></svg>No hidden fees. No interest. No hassle.</li>
  </ul>

  <section class="stats">
    <div class="stat"><div class="figure">Zero</div><div class="caption">Risk &amp; Administration<br>for you</div></div>
    <div class="stat"><div class="figure">30 / 45 / 60</div><div class="caption">Days of credit for your<br>customers</div></div>
    <div class="stat"><div class="figure">3 - 6%</div><div class="caption">Fully tax-deductable<br>expense</div></div>
  </section>

  <p class="payout-note">You receive up to 97% of the invoice amount within 24 hours.</p>

  <footer class="footer-bar">www.travicorfinance.com.au</footer>
</main>
</body>
</html>
```